IT Company dealing Business to Business website

Built on Wordpress
Professional eye-catching website, mobile friendly and responsive
We are currently in the process of re branding the company and refreshing the current image. The current website contains the necessary information about the company and services we provide. Also detailing companies we partner with.
We have a new logo and tag line which we are eager to incorporate into the new website.
We wish to have a fresh elegant business website which reflects our company value and delivers vital information for both old and new clients about what we provide in terms of service.
The website should be an extension of our offline media and an integrated company overview.

Target Market(s)

Businesses who require IT services

Industry/Entity Type

It Company

Coding

Coded - Design and coding required

Number of Pages Required

5+ page

Font styles to use
Sans Serif

Colors

Designer to choose colors to be used in the design.

Requirements
Must have
• Be made in Wordpress, and editable after without needing coding
• Mobile friendly/responsive
• Remote links to be displayed at the top of the web page
• Pay account and customer portal also displayed at the top of the web page
• Partners of the company to be displayed at the bottom of the screen
Nice to have
• Scrolling image in the centre, to be used for advertising services/features

```html
<!DOCTYPE html>
<html lang="en">
<head>
<meta charset="utf-8">
<title>Nexaport Solutions – IT Support Perth</title>
<link href="https://fonts.googleapis.com/css2?family=Nunito+Sans:wght@400;600;700&display=swap" rel="stylesheet">
<style>
:root{
  --blue:#1a6fc0;
  --blue-light:#2f8be0;
  --topbar:#3a3f47;
  --login:#2b2f35;
  --ink:#333a42;
  --muted:#6b727b;
  --pale:#f4f5f9;
  --white:#ffffff;
  --tab:#7d7f82;
  --footer:#262b31;
  --footer-line:#454b53;
  --card-shadow:0 2px 10px rgba(30,40,60,.12);
}
*{margin:0;padding:0;box-sizing:border-box}
html,body{width:1200px;height:2975px;overflow:hidden}
body{font-family:"Nunito Sans",Arial,sans-serif;color:var(--ink);background:var(--pale);position:relative}
.abs{position:absolute}
a{color:inherit;text-decoration:none}

/* top bar */
.topbar{left:0;top:0;width:1200px;height:30px;background:var(--topbar);font-size:11px;color:#d9dde2}
.topbar .contact{left:80px;top:8px}
.topbar .contact b{color:var(--blue-light);font-weight:600}
.topbar .login{left:873px;top:0;width:119px;height:30px;background:var(--login);color:#fff;text-align:center;line-height:30px;font-size:11px}
.topbar .pay{left:992px;top:0;width:125px;height:30px;background:var(--blue);color:#fff;text-align:center;line-height:30px;font-size:12px;font-weight:700}

/* nav */
.nav{left:0;top:30px;width:1200px;height:70px;background:var(--white)}
.brand{left:80px;top:22px;display:flex;align-items:center;gap:10px}
.brand .mark{width:24px;height:24px;background:var(--blue)}
.brand .name{font-size:22px;font-weight:700;color:var(--blue);letter-spacing:.5px}
.nav .menu{top:32px;font-size:10px;font-weight:700;letter-spacing:1px;color:#444}
.nav .menu.active{color:var(--blue);border-bottom:2px solid var(--blue);padding-bottom:3px}
.nav .remote{left:906px;top:32px;font-size:9px;letter-spacing:1px;color:#777}
.remote-btn{top:19px;width:32px;height:32px;border-radius:50%;border:1.5px solid var(--blue);background:#fff}
.remote-btn.on{background:var(--blue)}
.remote-btn::after{content:"";position:absolute;left:11px;top:11px;width:8px;height:8px;border-radius:2px;background:var(--blue)}
.remote-btn.on::after{background:#fff}

/* hero */
.hero{left:0;top:100px;width:1200px;height:645px;background:radial-gradient(ellipse at 55% 40%,#3f6e98 0%,#23405e 45%,#14212f 100%)}
.hero h1{left:0;top:186px;width:1200px;text-align:center;font-size:36px;font-weight:600;color:#fff}
.hero .lead{left:270px;top:240px;width:660px;text-align:center;font-size:18px;line-height:24px;color:#fff}
.btn{display:block;text-align:center;border-radius:18px;font-size:11px;font-weight:600}
.hero .explore{left:536px;top:312px;width:128px;height:34px;line-height:34px;background:#fff;color:var(--blue)}
.section-label{width:1200px;left:0;text-align:center;font-size:13px;color:var(--ink)}
.chev{display:block;margin:2px auto 0}
.hero .section-label{color:#fff}

/* services */
.services{left:131px;top:694px;width:936px;height:200px;background:var(--white)}
.svc{top:720px;width:280px;height:158px;background:linear-gradient(160deg,#6b7580,#2e3640);overflow:hidden}
.svc span{position:absolute;left:0;width:100%;top:68px;text-align:center;color:#fff;font-size:17px;font-weight:700}
.arrow{width:14px;height:14px}

/* about */
.about h2{left:232px;top:962px;font-size:27px;font-weight:400;color:var(--ink)}
.about h2 strong{color:var(--blue);font-weight:700}
.about p{left:232px;width:410px;font-size:11.5px;line-height:18px;color:#555}
.btn-outline{border:1.5px solid var(--blue);color:var(--blue);background:#fff}
.about .discover{left:232px;top:1214px;width:127px;height:32px;line-height:29px}
.about-brand{left:670px;top:1060px;display:flex;align-items:center;gap:18px}
.about-brand .sq{width:60px;height:60px;background:var(--blue)}
.about-brand .word{font-size:54px;font-weight:700;color:#7d7f82}
.divider{left:157px;top:1311px;width:886px;height:1px;background:#dfe2e8}

/* solutions */
.solutions{left:0;top:1398px;width:1200px;height:397px;background:var(--white)}
.tab{left:0;width:284px;height:79px;background:var(--tab);color:#fff;font-size:13px;line-height:79px;padding-left:78px}
.tab.active{background:var(--blue)}
.product{left:361px;top:1458px;width:278px;height:277px;background:linear-gradient(180deg,#e9ebef,#dcdfe5)}
.solution-title{left:686px;top:1484px;font-size:21px;font-weight:400;color:var(--ink)}
.solution-text{left:686px;top:1532px;width:480px;font-size:12.5px;line-height:20px;color:#555}
.readmore{left:686px;top:1676px;width:113px;height:32px;line-height:32px;background:var(--blue);color:#fff}

/* partners */
.partners-grid{left:157px;top:1932px;width:886px;height:190px;display:grid;grid-template-columns:repeat(3,1fr);grid-template-rows:repeat(2,1fr);gap:2px;background:#e6e8ec}
.partner{background:#fff;display:flex;align-items:center;justify-content:center}
.partner i{display:block;width:190px;height:34px;border-radius:4px;background:#c9ccd2}
.partner.raised{box-shadow:0 4px 14px rgba(0,0,0,.12)}
.partner.raised i{background:#a9c6e6}

/* updates */
.updates-bg{left:0;top:2187px;width:1200px;height:274px;background:var(--white)}
.updates h2{left:0;top:2240px;width:1200px;text-align:center;font-size:28px;font-weight:400;color:#4a5160}
.updates h2 strong{color:var(--blue);font-weight:700}
.post{top:2302px;width:280px;height:286px;background:#fff;box-shadow:var(--card-shadow)}
.post .thumb{position:absolute;left:0;top:0;width:280px;height:157px}
.post .tag{position:absolute;left:110px;top:147px;width:60px;height:20px;line-height:20px;text-align:center;font-size:10px;color:#fff;background:#f39c34}
.post h4{position:absolute;left:20px;top:188px;width:240px;text-align:center;font-size:12.5px;font-weight:600;line-height:19px;color:var(--ink)}
.post .date{position:absolute;left:0;top:244px;width:280px;text-align:center;font-size:10.5px;color:#888}

/* footer */
.footer{left:0;top:2461px;width:1200px;height:514px;background:var(--footer);color:#fff}
.fcol{top:2670px;width:300px;text-align:center;font-size:12px;line-height:18px;color:#fff}
.fcol .icon{display:block;margin:0 auto 14px}
.fcol .big{font-size:17px;line-height:22px;color:#fff}
.fcol .small{font-size:11px;color:#fff}
.fcol a{color:var(--blue-light);text-decoration:underline}
.vsep{top:2650px;width:0;height:130px;border-left:1px dashed #59606a}
.fline{left:157px;width:886px;height:1px;background:var(--footer-line)}
.fnav{top:2838px;font-size:9px;font-weight:700;letter-spacing:1px;color:#dfe2e6}
.fnav.active{color:var(--blue-light)}
.fsep{top:2838px;font-size:9px;color:#8b9199}
.copyright{left:157px;top:2926px;font-size:11px;color:#dfe2e6}
.copyright span{color:var(--blue-light)}
.social-label{left:856px;top:2926px;font-size:11px;color:#dfe2e6}
.social{top:2916px;width:32px;height:32px;border-radius:50%;border:1px solid #59606a}
.social.on{background:var(--blue);border-color:var(--blue)}
.social::after{content:"";position:absolute;left:12px;top:12px;width:6px;height:6px;border-radius:50%;background:#fff}
</style>
</head>
<body>

<header>
  <div class="abs topbar">
    <div class="abs contact"><b>Call Us:</b> (08) 9100 4020 &nbsp;&nbsp;&nbsp; <b>Email:</b> info@nexaport.net.au</div>
    <a class="abs login" href="#">&#9679; Login</a>
    <a class="abs pay" href="#">$ Pay Now!</a>
  </div>
  <nav class="abs nav">
    <div class="abs brand"><span class="mark"></span><span class="name">NEXAPORT</span></div>
    <a class="abs menu active" style="left:407px" href="#">HOME</a>
    <a class="abs menu" style="left:474px" href="#">IT SERVICES</a>
    <a class="abs menu" style="left:575px" href="#">SOLUTIONS</a>
    <a class="abs menu" style="left:672px" href="#">NEWS/BLOG</a>
    <a class="abs menu" style="left:772px" href="#">CONTACT US</a>
    <span class="abs remote">GET A REMOTE</span>
    <a class="abs remote-btn" style="left:1001px" href="#" aria-label="Remote for desktop"></a>
    <a class="abs remote-btn on" style="left:1045px" href="#" aria-label="Remote for laptop"></a>
    <a class="abs remote-btn" style="left:1087px" href="#" aria-label="Remote for mobile"></a>
  </nav>
</header>

<section class="abs hero" role="img" aria-label="Hands working on a laptop with glowing network technology icons overlaid">
  <h1 class="abs">Nexaport Solutions</h1>
  <p class="abs lead">Is a Perth IT support service providing businesses with complete IT support service solutions throughout Western Australia.</p>
  <a class="abs btn explore" href="#">Explore More</a>
  <div class="abs section-label" style="top:534px">Our Services
    <svg class="chev" width="10" height="6" viewBox="0 0 10 6"><path d="M1 1l4 4 4-4" fill="none" stroke="#fff" stroke-width="1.4"/></svg>
  </div>
</section>

<section class="services-area">
  <div class="abs services"></div>
  <div class="abs svc" style="left:157px" role="img" aria-label="Headphones resting on a laptop keyboard"><span>Professional IT services</span></div>
  <div class="abs svc" style="left:460px" role="img" aria-label="People working together at a desk"><span>IT management</span></div>
  <div class="abs svc" style="left:763px" role="img" aria-label="Businessman in a meeting"><span>Consultations</span></div>
  <svg class="abs arrow" style="left:122px;top:802px" viewBox="0 0 14 14"><path d="M9 2L4 7l5 5" fill="none" stroke="#666" stroke-width="1.5"/></svg>
  <svg class="abs arrow" style="left:1064px;top:802px" viewBox="0 0 14 14"><path d="M5 2l5 5-5 5" fill="none" stroke="#666" stroke-width="1.5"/></svg>
</section>

<section class="about">
  <h2 class="abs">IT Support <strong>Services Perth</strong></h2>
  <p class="abs" style="top:1024px">Nexaport Solutions is a Perth IT support service providing businesses with complete IT support service solutions throughout Western Australia.</p>
  <p class="abs" style="top:1090px">We provide IT support for small businesses through to medium sized enterprises to ensure they gain maximum benefit from their computing and IT environment. Keeping your equipment up to date and running smoothly is our focus so you can focus on your business...</p>
  <a class="abs btn btn-outline discover" href="#">Discover More</a>
  <div class="abs about-brand"><span class="sq"></span><span class="word">Nexaport</span></div>
  <div class="abs divider"></div>
  <div class="abs section-label" style="top:1332px">Our Solutions
    <svg class="chev" width="10" height="6" viewBox="0 0 10 6"><path d="M1 1l4 4 4-4" fill="none" stroke="#333" stroke-width="1.4"/></svg>
  </div>
</section>

<section class="abs solutions"></section>
<div class="abs tab" style="top:1398px">01 &nbsp;Cloud Suite</div>
<div class="abs tab" style="top:1478px">02 &nbsp;VOIP</div>
<div class="abs tab active" style="top:1558px">03 &nbsp;Draftline Review</div>
<div class="abs tab" style="top:1638px">04 &nbsp;Backups</div>
<div class="abs tab" style="top:1718px">05 &nbsp;Hardware</div>
<div class="abs product" role="img" aria-label="Three software product boxes in dark colours"></div>
<div class="solutions-copy">
  <h3 class="abs solution-title">Draftline Review</h3>
  <p class="abs solution-text">Built for technical professionals, Draftline Review allows users to create, markup and edit 2D and 3D PDFs. Digitize your workflows, streamline your processes and collaborate with project partners from anywhere, at anytime with Review. Review is available in 3 editions - Basic, Studio and Pro.</p>
  <a class="abs btn readmore" href="#">Read More</a>
</div>

<section class="partners">
  <div class="abs section-label" style="top:1857px">Our Partners
    <svg class="chev" width="10" height="6" viewBox="0 0 10 6"><path d="M1 1l4 4 4-4" fill="none" stroke="#333" stroke-width="1.4"/></svg>
  </div>
  <div class="abs partners-grid">
    <div class="partner"><i></i></div>
    <div class="partner raised"><i></i></div>
    <div class="partner"><i></i></div>
    <div class="partner"><i></i></div>
    <div class="partner"><i></i></div>
    <div class="partner"><i></i></div>
  </div>
  <svg class="abs arrow" style="left:122px;top:2018px" viewBox="0 0 14 14"><path d="M9 2L4 7l5 5" fill="none" stroke="#666" stroke-width="1.5"/></svg>
  <svg class="abs arrow" style="left:1064px;top:2018px" viewBox="0 0 14 14"><path d="M5 2l5 5-5 5" fill="none" stroke="#666" stroke-width="1.5"/></svg>
</section>

<div class="abs updates-bg"></div>
<footer class="abs footer"></footer>

<section class="updates">
  <h2 class="abs">Latest <strong>Updates</strong></h2>
  <article class="abs post" style="left:157px">
    <div class="thumb" role="img" aria-label="Glowing blue network of connected points" style="background:radial-gradient(circle at 50% 45%,#3b8ee8,#0b2a5a 75%)"></div>
    <span class="tag">Blog</span>
    <h4>IP Address of<br>Email Marketing Platforms</h4>
    <div class="date">December 21, 2016</div>
  </article>
  <article class="abs post" style="left:460px">
    <div class="thumb" role="img" aria-label="Hand holding a tablet showing charts" style="background:linear-gradient(135deg,#c9d6e4,#5c86ad)"></div>
    <span class="tag">News</span>
    <h4 style="text-decoration:underline">Nexaport Solutions<br>Achieves a Corelink Silver...</h4>
    <div class="date">Oct 1, 2015</div>
  </article>
  <article class="abs post" style="left:763px">
    <div class="thumb" role="img" aria-label="Colourful fibre optic light streaks" style="background:linear-gradient(135deg,#2a0f3a,#b2304a 50%,#e58a3a)"></div>
    <span class="tag">Blog</span>
    <h4>Delta SwitchLine<br>Switch setup for Web Access</h4>
    <div class="date">April 21, 2016</div>
  </article>
</section>

<section class="footer-content">
  <div class="abs fcol" style="left:148px">
    <svg class="icon" width="26" height="32" viewBox="0 0 26 32"><path d="M13 30S3 18 3 11a10 10 0 0120 0c0 7-10 19-10 19z" fill="none" stroke="var(--blue-light)" stroke-width="1.6"/><circle cx="13" cy="11" r="3.5" fill="none" stroke="var(--blue-light)" stroke-width="1.6"/></svg>
    Nexaport Solutions<br><span class="small">PO Box 2210 Riverton Bridge,<br>WA 6150</span>
  </div>
  <div class="abs vsep" style="left:448px"></div>
  <div class="abs fcol" style="left:450px">
    <svg class="icon" width="30" height="30" viewBox="0 0 30 30"><path d="M8 3l5 6-3 3c2 4 4 6 8 8l3-3 6 5-3 4C14 27 3 16 4 6z" fill="none" stroke="var(--blue-light)" stroke-width="1.6" stroke-linejoin="round"/></svg>
    <span class="big">Call: 08 9100 4020</span><br><span class="small">Fax: 08 9100 4030</span>
  </div>
  <div class="abs vsep" style="left:752px"></div>
  <div class="abs fcol" style="left:752px">
    <svg class="icon" width="30" height="30" viewBox="0 0 30 30"><circle cx="15" cy="15" r="12" fill="none" stroke="var(--blue-light)" stroke-width="1.6"/><circle cx="15" cy="15" r="6" fill="none" stroke="var(--blue-light)" stroke-width="1.6"/></svg>
    Need Help?<br><a href="#">info@nexaport.net.au</a><br><span class="small">Contact Us</span>
  </div>
  <div class="abs fline" style="top:2810px"></div>
  <a class="abs fnav active" style="left:362px" href="#">HOME</a>
  <span class="abs fsep" style="left:414px">|</span>
  <a class="abs fnav" style="left:440px" href="#">IT SERVICES</a>
  <span class="abs fsep" style="left:528px">|</span>
  <a class="abs fnav" style="left:550px" href="#">SOLUTIONS</a>
  <span class="abs fsep" style="left:642px">|</span>
  <a class="abs fnav" style="left:668px" href="#">NEWS/BLOG</a>
  <span class="abs fsep" style="left:756px">|</span>
  <a class="abs fnav" style="left:772px" href="#">CONTACT US</a>
  <div class="abs fline" style="top:2880px"></div>
  <div class="abs copyright">© 2017 <span>Nexaport Solutions</span>. All Rights Reserved</div>
  <div class="abs social-label">Get Social:</div>
  <a class="abs social" style="left:930px" href="#" aria-label="Social profile one"></a>
  <a class="abs social on" style="left:970px" href="#" aria-label="Social profile two"></a>
  <a class="abs social" style="left:1011px" href="#" aria-label="Social profile three"></a>
</section>

</body>
</html>
```